QVT Web Design Project

I would like a simple and elegant design for my international business consulting practice web site. I already have new QVT Logo and will have brochure-colors are blue, green and black

Practice areas:
I offer consulting services specializing in developing Internet-based anti-counterfeiting and anti-fraud programs, test purchases and investigations.

I offer Cyber Security, Data Protection and Compliance services

I also offer International Due Diligence Investigations and Country and Travel Risk Assessments

General Background Investigations

Physical Security Services

About me section listing my Bio

I have a set of key associates that I work with around the world and will want to list their CVs or Bios under "QVT

Associates"Banner with nice photo but not too cluttered

Ability to Upload documents and articles

Contact us section
Updates

I have uploaded my new logo-please advise if you didn't get it or it is not in the correct file format.

Thank you

Gordon

Hello Everyone,

Thank you for your submissions and ideas. I'm not sure about design only vs code. I understand that some of you do not do code-if not then please just provide design.

More about my business: see below link on Sharebox files to my brochure-this should help but don't use that phone number-see below.

https://files.sharebox.example/viewer?a=v&pid=explorer&srcid=0Q-4PX9nRfwqeMkTuZ3B8NHhsLWVmXy00ZWQ3LTkyOGQtZmQ1ZTg0YjE2OXB4&hl=en_US

 

Here are some details.

Contacts:

Gordon T. Falkirk, CPP

President

Falkirk and Associates, LLC

P.O. Box 41927

Gaithersburg, MD 20871

USA

web address:www.Falkirkandassociates.example (currently not working)

email:gord @falkirkand associates.example

Tel: 202-555-0147

I hope this is helpful. Gord

Reason: Sorry but during holiday period, have not had as much time to devote to this project. Thanks for your submissions.

Per my previous guidance, please keep designs simple and elegant and free from traditional security images with locks and chains-I prefer one or at most, two photos. Two colors- blue and green in addition to black for print. I want to present professional, corporate and international image. Thank you for your ideas nad submissions.

Gord

Target Market(s)

Law firms, large multi-national corporations, Security Industry

Industry/Entity Type

Business

Requirements
Must have
• Must have sections: (will provide text)

About QVT (will provide text)

Practice areas

Associates (will provide text)

Contact us

(it must also have ability to upload files and articles)
Should not have
• Old style fonts and symbols such as security badges, scales of justice, etc. I want a sleek and modern design.

```html
<!DOCTYPE html>
<html lang="en">
<head>
<meta charset="utf-8">
<title>QVT | Falkirk &amp; Associates, LLC</title>
<link rel="stylesheet" href="https://fonts.googleapis.com/css2?family=Noto+Sans:wght@400;700&family=Oswald:wght@400;500&family=Arimo&family=Tinos&display=swap">
<style>
:root{
  --blue:#1a5ea8;
  --blue-dark:#0f4c8e;
  --nav-top:#2a73c0;
  --nav-bottom:#0d55a2;
  --green:#4f8f1a;
  --green-light:#7cc13a;
  --text:#555;
  --link:#2a86c4;
  --black:#000;
}
*{box-sizing:border-box;margin:0;padding:0}
html,body{width:996px;height:1200px;overflow:hidden;background:#fff}
body{position:relative;font-family:"Noto Sans",sans-serif;color:var(--text)}
.abs{position:absolute}

/* header */
.share-bar{top:16px;right:11px;display:flex;gap:6px}
.share-btn{height:19px;border:1px solid #c9c9c9;border-radius:3px;background:linear-gradient(#fff,#e9e9e9);font:11px "Arimo",sans-serif;color:#333;display:flex;align-items:center;gap:4px;padding:0 5px}
.share-btn i{width:11px;height:11px;background:var(--blue);display:block}
.share-count{height:19px;min-width:16px;border:1px solid #c9c9c9;background:#fff;font:10px "Arimo",sans-serif;display:flex;align-items:center;justify-content:center;margin-left:-4px}
.share-btn.hot{background:#e8623a;border-color:#d5532c;color:#fff}
.share-btn.hot i{background:#fff}

.brand{top:38px;left:12px;color:var(--blue)}
.brand-name{font:400 32px/1 "Noto Sans",sans-serif;letter-spacing:.2px}
.brand-tag{margin-top:13px;font:400 19px/1 "Noto Sans",sans-serif;letter-spacing:3.4px;color:var(--blue)}

.callme{top:58px;right:14px;font:400 34px/1 "Oswald",sans-serif;transform:scaleX(.78);transform-origin:right center;color:#111;white-space:nowrap}
.callme span{color:var(--blue)}
.callme-shade{top:98px;left:756px;width:232px;height:14px;background:radial-gradient(ellipse at top,rgba(0,0,0,.14),rgba(0,0,0,0) 70%)}

/* nav */
.main-nav{top:145px;left:11px;width:975px;height:44px;display:flex;background:linear-gradient(var(--nav-top),var(--nav-bottom))}
.main-nav a{height:44px;display:flex;align-items:center;justify-content:center;color:#fff;text-decoration:none;font-size:14px;border-right:1px solid rgba(255,255,255,.25)}
.main-nav a:last-child{border-right:0}

/* sidebar */
.side-nav{top:197px;left:11px;width:182px;background:#e1e1e1}
.side-nav a{display:block;height:32px;line-height:32px;padding-left:16px;font-size:12.5px;color:#444;text-decoration:none;border-bottom:1px solid #fff;background:linear-gradient(#e9e9e9,#d9d9d9)}

/* banner */
.banner{top:196px;left:201px;width:784px;height:260px;border:1px solid #c8c8c8;padding:3px}
.banner-photo{position:relative;width:100%;height:100%;background:linear-gradient(90deg,#cdd3ce 0%,#b9c2bd 35%,#9aa5a2 60%,#d6dfe4 100%)}
.banner-head{position:absolute;left:14px;top:126px;font:400 31px/35px "Oswald",sans-serif;color:#4a7d12;transform:scaleX(.78);transform-origin:left;white-space:nowrap}
.banner-btn{position:absolute;left:16px;top:209px;width:136px;height:31px;background:linear-gradient(var(--green-light),var(--green));border:1px solid #3f7a12;color:#fff;font-size:17px;display:flex;align-items:center;justify-content:center;gap:8px}

/* features */
.features{top:466px;left:11px;width:975px;height:188px;border:1px solid #c8c8c8;background:linear-gradient(#eef3f7,#fafcfd 45%,#e9eef2)}
.feature{position:absolute;top:0;width:310px}
.feature svg{position:absolute;top:16px}
.feature h3{position:absolute;top:18px;font:400 28px/1 "Oswald",sans-serif;color:var(--blue);transform:scaleX(.72);transform-origin:left;white-space:nowrap;text-shadow:1px 1px 0 #fff}
.feature p{position:absolute;top:66px;font-size:13.4px;line-height:16.5px;color:#555}
.more{font:11px "Arimo",sans-serif;color:#222;display:flex;align-items:center;gap:6px}
.more:before{content:"";border-left:4px solid #333;border-top:3px solid transparent;border-bottom:3px solid transparent}
.feature .more{position:absolute;top:153px}

/* welcome */
.section-title{font:400 18px/1 "Noto Sans",sans-serif;color:#333}
.section-title b{font-weight:400;color:var(--blue);font-size:23px}
.welcome{top:686px;left:11px;width:626px}
.welcome .section-title{padding-bottom:10px;border-bottom:1px dashed #aaa}
.welcome p{margin-top:12px;font:12px/18px "Arimo",sans-serif;color:#555}
.welcome p+p{margin-top:18px}
.welcome .more{margin-top:14px}

.services{top:686px;left:681px;width:305px}
.services .section-title{padding:0 0 10px 0}
.shade-line{height:8px;background:radial-gradient(ellipse at top,rgba(0,0,0,.13),rgba(0,0,0,0) 70%)}
.services ul{list-style:none;margin-top:12px}
.services li{height:31px;font-size:13px;color:#444;display:flex;align-items:center;gap:16px;padding-left:0;white-space:nowrap}
.services .more{position:absolute;right:0;top:224px}

/* bottom */
.col-title{font:400 18px/1 "Noto Sans",sans-serif;color:var(--blue);padding-bottom:11px}
.dotted{border-bottom:1px dashed #aaa}
.docs{top:950px;left:11px;width:286px}
.news{top:950px;left:339px;width:245px}
.link-list{list-style:none;margin-top:10px}
.link-list li{display:flex;gap:10px;font:12px/14px "Arimo",sans-serif;color:var(--link);margin-bottom:15px;padding-left:10px}
.link-list li:before{content:"»";color:#7a9fbe;font-size:13px}
.docs .link-list li{margin-bottom:15.5px}
.contact{top:950px;left:703px;width:283px}
.contact-row{display:flex;align-items:center;gap:6px;padding-left:8px}
.contact-phone{margin-top:2px;font:400 25px/1 "Tinos",serif;color:var(--blue-dark)}
.contact-mail{margin-top:8px;font:700 13px/1 "Tinos",serif;color:var(--blue-dark);white-space:nowrap}

.footer{top:1140px;left:11px;width:975px;height:49px;background:var(--black);border:1px solid #6aa7d8;color:#fff;font:12px "Arimo",sans-serif;display:flex;align-items:center;justify-content:center}
</style>
</head>
<body>

<div class="abs share-bar">
  <span class="share-btn"><i></i>Share</span>
  <span class="share-btn"><i></i>Post</span><span class="share-count">0</span>
  <span class="share-btn" style="margin-left:26px"><i></i>Vote</span><span class="share-count">0</span>
  <span class="share-btn"><i></i>Like</span>
  <span class="share-btn hot" style="margin-left:26px"><i></i>Share</span>
</div>

<div class="abs brand">
  <div class="brand-name">QVT Falkirk &amp; Associates, LLC</div>
  <div class="brand-tag">Intellectual Property and Cyber Security</div>
</div>

<div class="abs callme">CALL ME : <span>202-555-0147</span></div>
<div class="abs callme-shade"></div>

<nav class="abs main-nav">
  <a style="width:109px">About Us</a>
  <a style="width:134px">Solutions</a>
  <a style="width:146px">Case Studies</a>
  <a style="width:104px">QVT</a>
  <a style="width:124px">Insights</a>
  <a style="width:129px">Careeres</a>
  <a style="width:102px">FAQs</a>
  <a style="width:127px">Contact Us</a>
</nav>

<aside class="abs side-nav">
  <a>Cybersecurity</a>
  <a>Cybersecurity Home</a>
  <a>Solutions</a>
  <a>Case Studies</a>
  <a>Insights</a>
  <a>Press Releases</a>
  <a>Public Sector</a>
  <a>Contact Cybersecurity</a>
</aside>

<section class="abs banner">
  <div class="banner-photo" role="img" aria-label="Photo of two colleagues working together at a laptop in a bright office">
    <div class="banner-head">Data Loss Prevention, Cyber Security,<br>Compliance services</div>
    <div class="banner-btn">Learn More
      <svg width="7" height="10" viewBox="0 0 7 10"><path d="M0 0L7 5L0 10Z" fill="#fff"/></svg>
    </div>
  </div>
</section>

<section class="abs features">
  <div class="feature" style="left:0">
    <svg style="left:4px" width="36" height="40" viewBox="0 0 36 40">
      <path d="M18 1L34 7V18C34 29 27 36 18 39C9 36 2 29 2 18V7Z" fill="#5aa02c" stroke="#3d7a18"/>
      <path d="M10 20L16 26L27 13" stroke="#fff" stroke-width="4" fill="none" stroke-linecap="round" stroke-linejoin="round"/>
    </svg>
    <h3 style="left:50px">CYBER SECURITY</h3>
    <p style="left:52px;width:262px">Lorem ipsum dolor sit amet, consectetur adipiscing elit. Suspendisse ut eleifend orci. Phasellus eu sem a lectus tempus congue a lacinia elit. Integer tincidunt,</p>
    <span class="more" style="left:53px">Learn More</span>
  </div>
  <div class="feature" style="left:322px">
    <svg style="left:0" width="40" height="34" viewBox="0 0 40 34">
      <rect x="1" y="6" width="38" height="26" rx="3" fill="#c9a64a" stroke="#6b5a2a"/>
      <rect x="1" y="6" width="38" height="7" fill="#3a3a3a"/>
      <circle cx="20" cy="21" r="7" fill="#eee" stroke="#333" stroke-width="2"/>
      <circle cx="20" cy="21" r="2.5" fill="#333"/>
    </svg>
    <h3 style="left:50px">Data Protection</h3>
    <p style="left:50px;width:262px">Lorem ipsum dolor sit amet, consectetur adipiscing elit. Suspendisse ut eleifend orci. Phasellus eu sem a lectus tempus congue a lacinia elit. Integer tincidunt,</p>
    <span class="more" style="left:50px">Learn More</span>
  </div>
  <div class="feature" style="left:655px">
    <svg style="left:0" width="42" height="42" viewBox="0 0 42 42">
      <path d="M2 10L34 4L38 36L6 40Z" fill="#f3d21c" stroke="#b59a10"/>
      <circle cx="18" cy="20" r="5" fill="#333"/>
      <circle cx="27" cy="28" r="3.5" fill="#333"/>
    </svg>
    <h3 style="left:60px">COMPLIANCE SERVICES</h3>
    <p style="left:60px;width:262px">Lorem ipsum dolor sit amet, consectetur adipiscing elit. Suspendisse ut eleifend orci. Phasellus eu sem a lectus tempus congue a lacinia elit. Integer tincidunt,</p>
    <span class="more" style="left:60px">Learn More</span>
  </div>
</section>

<section class="abs welcome">
  <h2 class="section-title">Welcome to&nbsp; <b>QVT | Falkirk &amp; Associates, LLC</b></h2>
  <p>Integer suscipit, neque quis dignissim pellentesque, augue turpis auctor tortor, sed gravida arcu orci nec lectus. Cras sed rutrum magna. Proin nec augue neque, sed sagittis lacus. Lorem ipsum dolor sit amet, consectetur adipiscing elit. Aenean ornare, quam quis porttitor faucibus, augue mi vehicula elit, sed feugiat dui mauris a arcu. Suspendisse sit amet est sed sem tempor porta eu eget enim. Sed venenatis, magna id pretium luctus, nibh risus bibendum urna, vitae aliquet eros sapien ut est.</p>
  <p>Integer suscipit, neque quis dignissim pellentesque, augue turpis auctor tortor, sed gravida arcu orci nec lectus. Cras sed rutrum magna. Proin nec augue neque, sed sagittis lacus. Lorem ipsum dolor sit amet, consectetur adipiscing elit. Aenean ornare, quam quis porttitor faucibus, augue mi vehicula elit.Integer suscipit, neque quis</p>
  <span class="more">Read More</span>
</section>

<section class="abs services">
  <h2 class="section-title" style="padding-left:19px">Other&nbsp; <b>Services</b></h2>
  <div class="shade-line"></div>
  <ul>
    <li><svg width="10" height="10" viewBox="0 0 10 10"><path d="M5 0L10 5L5 10L0 5Z" fill="#3f8a2a"/><circle cx="5" cy="5" r="1.5" fill="#fff"/></svg>International Due Diligence Investigations</li>
    <li><svg width="10" height="10" viewBox="0 0 10 10"><path d="M5 0L10 5L5 10L0 5Z" fill="#3f8a2a"/><circle cx="5" cy="5" r="1.5" fill="#fff"/></svg>Country and Travel Risk Assessments</li>
    <li><svg width="10" height="10" viewBox="0 0 10 10"><path d="M5 0L10 5L5 10L0 5Z" fill="#3f8a2a"/><circle cx="5" cy="5" r="1.5" fill="#fff"/></svg>General Background Investigations</li>
    <li><svg width="10" height="10" viewBox="0 0 10 10"><path d="M5 0L10 5L5 10L0 5Z" fill="#3f8a2a"/><circle cx="5" cy="5" r="1.5" fill="#fff"/></svg>Physical Security Services</li>
    <li><svg width="10" height="10" viewBox="0 0 10 10"><path d="M5 0L10 5L5 10L0 5Z" fill="#3f8a2a"/><circle cx="5" cy="5" r="1.5" fill="#fff"/></svg>Proin eget purus augue.</li>
  </ul>
  <span class="more">Read More</span>
</section>

<section class="abs docs">
  <h2 class="col-title dotted">Documentation</h2>
  <ul class="link-list">
    <li>Lorem ipsum dolor sit amet, adipiscing elit.</li>
    <li>Integer ornare nulla sed leo posuere eu a sem.</li>
    <li>Ut sagittis nisi ac nunc molestie varius.</li>
    <li>Praesent cursus nisi iaculis ut sodales purus</li>
  </ul>
</section>

<section class="abs news">
  <h2 class="col-title dotted">Latest News</h2>
  <ul class="link-list">
    <li>Lorem ipsum dolor sit amet, consectetur adipiscing elit.</li>
    <li>Integer ornare nulla sed leo posuere eu accumsan sem auctor.</li>
    <li>Ut sagittis nisi ac nunc molestie varius.</li>
  </ul>
  <span class="more" style="margin-top:-4px;padding-left:4px">Read More News</span>
</section>

<section class="abs contact">
  <h2 class="col-title" style="padding-left:20px;padding-bottom:8px">Contact Us</h2>
  <div class="shade-line"></div>
  <div class="contact-row contact-phone">
    <svg width="34" height="30" viewBox="0 0 34 30">
      <rect x="2" y="4" width="30" height="24" rx="6" fill="#f0a020" stroke="#b06a10"/>
      <path d="M11 11c0 6 5 11 11 11l3-3-4-3-2 2c-2-1-4-3-5-5l2-2-3-4z" fill="#333"/>
    </svg>
    202-555-0147
  </div>
  <div class="contact-row contact-mail">
    <svg width="34" height="26" viewBox="0 0 34 26">
      <rect x="3" y="5" width="28" height="18" fill="#4aa3df" stroke="#1f6fa8"/>
      <path d="M3 5L17 16L31 5" stroke="#fff" stroke-width="2" fill="none"/>
    </svg>
    gord @falkirkand associates.example
  </div>
</section>

<footer class="abs footer">© 2011, All Rights Reserved</footer>

</body>
</html>
```